Flyer for handout on the street to attract people

Create two different leaflets for handing out to recruit volunteers to participate in a program of biological specimen donation. The leaflet should be catchy, have some graphics, and have enough info that people will want to sign up by going to the website for more information.

Leave room on each leaflet for some English and Chinese. The example of Leaflet #1 will need approximately the same space in order to have the Chinese translation.

The example of Leaflet #2 already has a Chinese translation which can be incorporated.

The size should be half of A4 page. If it is a whole A4 page it may also be considered.

Leaflet #1 Text:

RECRUITING HEALTHY VOLUNTEERS (and get PAID)!

The Orient Florabase Vault is recruiting healthy individuals in Hong Kong to participate in a scientific research project to study bacteria in healthy guts. They will pay you $200 HKD per day to participate in the study. If you qualify, you can earn up to $4800 a month!

Incidences of digestive and colon diseases are increasing rapidly in Hong Kong, and part of the key to solving this problem is understanding gut bacteria. There are up to 100 trillion bacteria and microbes in every human gut, including yours. Scientists have recently uncovered that these bacteria are key human digestion and immune systems. However, when your gut bacteria are imbalanced, it can cause all kinds of problems such as indigestion, IBS, ulcerative colitis, or clostridium difficile infection.

Every year, more than 500,000 people are infected by a toxic bacteria called clostridium difficile, which causes severe stomach pain, and sometimes even death. YOUR GUT BACTERIA COULD BE KEY TO HELPING THESE SICK PATIENTS.

CRITERIA FOR PARTICIPATING: If you are a healthy adult between 18-50 years old; no digestive problems and no recent medications, then the Orient VitaVault needs your participation! They will pay you $200 HKD per day to participate in the study. If you qualify, you can earn up to $4800 a month! To learn more information, go to http://www.orientvitavault.example or send a whatsapp to 6734 2098

Leaflet #2 Text:

Get paid to give your poopoo!

Literally.

Asia’s first commercial stool bank is recruiting donors. Get paid up to $4,800 HKD per month for your poop donations at our convenient Central Hong Kong lab.

Answer the questionnaire to see if you qualify at www.orientvitavault.example or call 6734 2098 for more information.

你好屎!

我地就係想要你D好屎。

全亞洲第一間商業糞便銀行正招募捐贈者。請即前往我們位於中環的糞便銀行成為捐贈者,每月最多可賺取6,000港元的酬勞。

想知道自己是否適合捐贈?馬上點擊 www.orientvitavault.example/donate 回答問題或撥打7382-4615查詢詳情。

Target Market(s)

Young professionals, middle-class

Industry/Entity Type

Medical

Font styles to use
Serif
Sans Serif
Decorative

Requirements
Must have
• The text. Two leaflet examples. Some graphics.
Nice to have
• Catchy design. Something people will see while walking past and go ahead and take it from someone handing out flyers.
Should not have
• Only text. Should be colorful and have graphics. (Can download or shutterstock photos.)

```html
<!DOCTYPE html>
<html lang="en">
<head>
<meta charset="utf-8">
<title>Recruiting Healthy Volunteers</title>
<link href="https://fonts.googleapis.com/css2?family=Arvo:wght@400;700&family=Philosopher:ital,wght@0,700;1,700&display=swap" rel="stylesheet">
<style>
  :root {
    --page-bg: #d6d6d8;
    --paper-top: #eef5f8;
    --paper-bottom: #cfe4ec;
    --royal: #1c2a9c;
    --royal-deep: #16208a;
    --swoosh-grey: #7c7c7e;
    --band: #575aa2;
    --ink: #3e3e44;
    --muted: #8a8a8e;
    --white: #ffffff;
    --photo-light: #e9ecef;
    --photo-mid: #b8c3cc;
    --chat: #3bb54a;
  }
  * { margin: 0; padding: 0; box-sizing: border-box; }
  html, body { width: 1200px; height: 911px; overflow: hidden; }
  body { background: var(--page-bg); position: relative; }

  .flyer {
    position: absolute;
    left: 260px; top: 10px;
    width: 680px; height: 891px;
    background: linear-gradient(180deg, var(--paper-top) 0%, var(--paper-bottom) 100%);
    overflow: hidden;
    box-shadow: 0 4px 14px rgba(0,0,0,.18);
  }

  .hero { position: absolute; left: 0; top: 0; width: 680px; height: 345px; }

  .brand {
    position: absolute; left: 26px; top: 30px;
    display: flex; align-items: center; gap: 8px;
    font-family: "Arvo", serif; font-size: 14px; color: var(--royal);
  }
  .brand-dot { width: 22px; height: 22px; border-radius: 50%; background: var(--royal); }

  .content {
    position: absolute; left: 0; top: 340px; width: 680px;
    display: flex; flex-direction: column; align-items: center;
  }

  .headline { text-align: center; font-family: "Philosopher", sans-serif; }
  .headline-main {
    font-size: 35px; font-weight: 700; color: var(--royal);
    letter-spacing: .5px; line-height: 1.1; white-space: nowrap;
  }
  .headline-sub {
    font-size: 30px; font-style: italic; font-weight: 700;
    color: var(--muted); line-height: 1.15;
  }

  .story {
    width: 620px; margin-top: 12px;
    font-family: "Arvo", serif; font-size: 11.6px; line-height: 1.4; color: var(--ink);
  }
  .story p + p { margin-top: 7px; }
  .story .amount { color: var(--royal); font-weight: 700; }

  .tagline {
    width: 620px; margin-top: 10px;
    font-family: "Philosopher", sans-serif; font-style: italic; font-weight: 700;
    font-size: 15px; color: var(--royal); text-align: center; letter-spacing: .2px;
  }

  .criteria {
    width: 680px; margin-top: 12px;
    background: var(--band); color: var(--white);
    padding: 12px 34px 14px;
    text-align: center;
  }
  .criteria-title { font-family: "Philosopher", sans-serif; font-weight: 700; font-size: 25px; letter-spacing: .5px; }
  .criteria-text { font-family: "Arvo", serif; font-size: 12px; line-height: 1.45; margin-top: 4px; }
  .criteria-text strong { display: block; font-size: 14px; margin-top: 2px; }

  .contact {
    width: 680px; margin-top: 12px;
    text-align: center; font-family: "Arvo", serif; color: var(--ink);
  }
  .contact-lead { font-size: 25px; font-weight: 700; color: var(--muted); }
  .contact-line {
    font-size: 13px; margin-top: 6px;
    display: flex; justify-content: center; align-items: center; gap: 6px;
  }
  .contact-line b { font-weight: 700; }
  .contact-or { color: var(--royal); font-weight: 700; font-size: 15px; margin: 0 8px; }
  .chat-dot { width: 12px; height: 12px; border-radius: 50%; background: var(--chat); display: inline-block; }
</style>
</head>
<body>
  <main class="flyer">
    <svg class="hero" viewBox="0 0 680 345">
      <defs>
        <linearGradient id="photoTone" x1="0" y1="0" x2="1" y2="1">
          <stop offset="0" stop-color="#dfe4e8"/>
          <stop offset=".5" stop-color="#b8c3cc"/>
          <stop offset="1" stop-color="#8fb2d4"/>
        </linearGradient>
      </defs>
      <ellipse cx="70" cy="60" rx="230" ry="170" fill="#e9ecef"/>
      <path role="img" aria-label="Photo of three smiling doctors and nurses looking at a tablet in a hospital corridor"
            d="M150,0 H600 Q640,250 60,335 Q170,230 170,120 Q170,50 150,0 Z" fill="url(#photoTone)"/>
      <path d="M600,0 H622 Q655,275 40,340 Q520,270 600,0 Z" fill="#7c7c7e"/>
      <path d="M622,0 H665 Q690,300 0,345 L0,342 Q610,290 622,0 Z" fill="#16208a"/>
    </svg>

    <div class="brand"><span class="brand-dot"></span>Orient Florabase Vault</div>

    <div class="content">
      <header class="headline">
        <h1 class="headline-main">RECRUITING HEALTHY VOLUNTEERS</h1>
        <p class="headline-sub">(and get PAID)!</p>
      </header>

      <section class="story">
        <p>The Orient Florabase Vault is recruiting healthy individuals in Hong Kong to participate in a scientific research project to study bacteria in healthy guts. They will pay you <span class="amount">$200</span> HKD per day to participate in the study. If you qualify, you can earn up to <span class="amount">$4800</span> a month!</p>
        <p>Incidences of digestive and colon diseases are increasing rapidly in Hong Kong, and part of the key to solving this problem is understanding gut bacteria. There are up to 100 trillion bacteria and microbes in every human gut, including yours. Scientists have recently uncovered that these bacteria are key human digestion and immune systems. However, when your gut bacteria are imbalanced, it can cause all kinds of problems such as indigestion, IBS, ulcerative colitis, or clostridium difficile infection.</p>
        <p>Every year, more than 500,000 people are infected by a toxic bacteria called clostridium difficile, which causes severe stomach pain, and sometimes even death.</p>
      </section>

      <p class="tagline">YOUR GUT BACTERIA COULD BE KEY TO HELPING THESE SICK PATIENTS.</p>

      <section class="criteria">
        <h2 class="criteria-title">CRITERIA FOR PARTICIPATING:</h2>
        <p class="criteria-text">If you are a healthy adult between 18-50 years old; no digestive problems and no recent medications, then the Orient VitaVault needs your participation! They will pay you $200 HKD per day to participate in the study. If you qualify, you can earn up to <strong>$4800 a month!</strong></p>
      </section>

      <footer class="contact">
        <p class="contact-lead">To learn more information,</p>
        <p class="contact-line">
          <span>go to</span>
          <svg width="12" height="12" viewBox="0 0 12 12" aria-hidden="true">
            <circle cx="6" cy="6" r="5" fill="none" stroke="#3e3e44" stroke-width="1.2"/>
            <ellipse cx="6" cy="6" rx="2.2" ry="5" fill="none" stroke="#3e3e44" stroke-width="1"/>
            <line x1="1" y1="6" x2="11" y2="6" stroke="#3e3e44" stroke-width="1"/>
          </svg>
          <span>www.<b>orientvitavault</b>.example</span>
          <span class="contact-or">OR</span>
          <span class="chat-dot"></span>
          <span>to <b>6734 2098</b></span>
        </p>
      </footer>
    </div>
  </main>
</body>
</html>
```